Brackenmoor Aerosol Label Design

We would preferably like it if you have had existing experience with aerosol labels.
We are an automotive & industrial supplies company looking to update our image and general product theme, our website is www.brackenmoorstore.com.au Starting with our trim and dashboard enhancer aerosol we would like to completely revamp our range of products to reflect a more modern and creative flashy look. We have attached an image of our old and outdated label and our logo. Please use the old label for the product name, part number, can size, problems & causes, features & benefits and all the safety information. Our address is now 7/318 Kestrel Avenue, Ferncliff VIC 3187 and our phone number is +61 3 9184 5362.
We also need to update the product for GHS labelling. Please remove the recycle and flammable gas logo and replace with the attached red diamonds.
Size of the printed label will be 180x207mm (Height x Width)
Be creative with this whilst maintaining a professional image. Keep in mind this is a product for shining and detailing dashboards, trims, rubber materials. We like the idea of a graphic on the front for easy identification when the product is on the shelf. It’s important to us that we stand out from the crowd and are leaders not followers. We have also attached some examples from another project on craft hive. Feel free to contact us at anytime for more info. We have uploaded some examples of the styles of labels we like.

Target Market(s)

Automotive workshops and car enthusiasts, any age group

Industry/Entity Type

Automotive

Font styles to use
Sans Serif

Requirements
Must have
• Must have our updated address, phone numbers, website and GHS labelling
Nice to have
• A feature graphic on the front of the can like the attached labels, a graphic would be nicer than a picture.
Should not have
• Too many colours and not be confusing, our product needs to be easily distinguished when sitting on the shelf in comparison to our competitors.

```html
<!DOCTYPE html>
<html lang="en">
<head>
<meta charset="utf-8">
<title>Brackenmoor Trim &amp; Dashboard Enhancer – Label</title>
<link rel="stylesheet" href="https://fonts.googleapis.com/css2?family=Lato:wght@400;700;900&family=Montserrat:wght@700;800&display=swap">
<style>
  :root {
    --canvas: #ffffff;
    --label-grey: #2e2e2e;
    --panel-black: #1c1c1c;
    --brand-yellow: #f5c518;
    --bleed-blue: #2aa7d6;
    --text-light: #e6e6e6;
    --heading-grey: #a8a8a8;
    --ghs-red: #d71920;
  }
  * { margin: 0; padding: 0; box-sizing: border-box; }
  html, body { width: 1200px; height: 800px; overflow: hidden; background: var(--canvas); }
  .canvas { position: relative; width: 1200px; height: 800px; }

  .label {
    position: absolute; left: 179px; top: 30px;
    width: 813px; height: 715px;
    background: var(--label-grey);
    transform: scale(1.035); transform-origin: top left;
    font-family: "Lato", sans-serif; color: var(--text-light);
  }
  .label__strip { position: absolute; left: 0; top: 0; width: 71px; height: 685px; background: var(--brand-yellow); }
  .label__front { position: absolute; left: 71px; top: 0; width: 297px; height: 685px; background: var(--panel-black); }
  .label__bleed { position: absolute; left: 8px; top: 8px; width: 797px; height: 694px; border: 1px solid var(--bleed-blue); border-radius: 6px; pointer-events: none; }

  .front-mascot {
    position: absolute; left: 88px; top: 40px; width: 120px; height: 125px;
    background: radial-gradient(circle at 50% 45%, #3a3a3a, var(--panel-black) 70%);
  }
  .front-brand {
    position: absolute; left: 0; top: 172px; width: 297px; text-align: center;
    font-family: "Montserrat", sans-serif; font-weight: 800; font-size: 21px;
    color: var(--brand-yellow); letter-spacing: 0.5px;
  }
  .front-title {
    position: absolute; left: 0; top: 240px; width: 297px; text-align: center;
    font-family: "Montserrat", sans-serif; font-weight: 800; font-size: 31px; line-height: 1.08;
    color: var(--brand-yellow);
  }
  .front-graphic {
    position: absolute; left: 0; top: 378px; width: 297px; height: 250px;
    background: linear-gradient(160deg, rgba(184,144,42,0) 10%, rgba(184,144,42,0.35) 55%, rgba(184,144,42,0.12) 90%);
  }
  .front-size {
    position: absolute; left: 0; top: 652px; width: 297px; text-align: center;
    font-weight: 900; font-size: 15px; letter-spacing: 1.5px; color: var(--brand-yellow);
  }

  .info { position: absolute; left: 381px; top: 16px; width: 414px; font-size: 9.2px; line-height: 1.38; }
  .info__title { font-size: 14px; font-weight: 700; color: var(--text-light); margin-bottom: 1px; }
  .info p { margin-bottom: 7px; }
  .info .gap { margin-top: 13px; }
  .info__head { font-weight: 700; color: var(--heading-grey); font-size: 10.5px; }
  .info .narrow { width: 292px; }

  .ghs { position: absolute; left: 703px; width: 86px; height: 86px; }
  .ghs--exclaim { top: 312px; }
  .ghs--flame { top: 408px; }
  .ghs-note {
    position: absolute; left: 690px; width: 112px; text-align: center;
    font-family: "Montserrat", sans-serif; font-weight: 700; font-size: 8.6px; line-height: 1.45; color: #ffffff;
  }
  .ghs-note--flame { top: 502px; }
  .ghs-note--un { top: 540px; }

  .back-mascot {
    position: absolute; left: 418px; top: 598px; width: 80px; height: 72px;
    background: radial-gradient(circle at 50% 45%, #4a4a4a, var(--label-grey) 70%);
  }
  .back-brand {
    position: absolute; left: 398px; top: 672px; width: 120px; text-align: center;
    font-family: "Montserrat", sans-serif; font-weight: 800; font-size: 11px; color: var(--brand-yellow);
  }
  .company {
    position: absolute; right: 25px; top: 612px; text-align: right;
    font-size: 8.4px; line-height: 1.32; color: var(--text-light); font-style: normal;
  }
  .company__code { font-size: 7px; }
</style>
</head>
<body>
<main class="canvas">
  <section class="label">
    <div class="label__strip"></div>

    <div class="label__front">
      <div class="front-mascot" role="img" aria-label="Brand mascot illustration"></div>
      <div class="front-brand">BRACKENMOOR</div>
      <h1 class="front-title">TRIM<br>&amp;<br>DASHBOARD<br>ENHANCER</h1>
      <div class="front-graphic" role="img" aria-label="Gold line illustration of a car dashboard and steering wheel"></div>
      <div class="front-size">350g</div>
    </div>

    <div class="info">
      <h2 class="info__title">Brackenmoor Trim &amp; Dashboard Enhancer</h2>
      <p><span class="info__head">PROBLEMS &amp; CAUSES:</span> Deterioration of vinyl, rubber mouldings and plastic parts due to age and weathering can cause car trim to look worn and dull. Hinges and moving parts can become restricted due to lack of lubrication.</p>
      <p><span class="info__head">FEATURES &amp; BENEFITS:</span> Brackenmoor Trim &amp; Dashboard Enhancer is a dry, non greasy formula which will restore faded and worn car trim, dashboards, doors, rubber mouldings and similar surfaces. Its' unique qualities also act to protect surfaces from sunlight and weathering. Brackenmoor Trim &amp; Dashboard Enhancer can also be used to lubricate and protect hinges, slides, locks and electrical and mechanical equipment. The dry satin finish resists attraction of dust and grime.</p>
      <p class="gap"><span class="info__head">CAUTION: KEEP OUT OF REACH OF CHILDREN</span></p>
      <p class="gap"><span class="info__head">DIRECTIONS FOR USE:</span> Shake can well before using. Ensure surface is clean and free from grit and grime. Spray surface from distance of 15 to 20 centimetres, avoiding painted surfaces. Large areas may require wiping after application.</p>
      <p class="gap"><span class="info__head">SAFETY DIRECTIONS:</span> Do not puncture, or incinerate can, even when empty. Intentional misuse by deliberately concentrating and inhaling contents can be harmful or fatal, irritating to eyes.</p>
      <p class="gap narrow"><span class="info__head">FIRST AID:</span> If poisoning occurs, or for advice, contact a doctor or Poisons Information Centre on 13 42 58 (Australia) or 0800 519 803 (New Zealand). If in eyes flush with plenty of water for 15 minutes and seek medical attention immediately, Toxic if swallowed.<br>If swallowed, do not induce vomiting. Drink one glass of water.</p>
      <p class="narrow"><span class="info__head">FLAMMABLE:</span> Do not store or use near fire or flame.</p>
      <p class="narrow"><span class="info__head">EMERGENCY PROCEDURES:</span> Keep away from heat, sparks, flame and other sources of ignition. Wear all appropriate personal protective equipment during use. Avoid skin and eye contact Use with adequate ventilation. Avoid breathing vapours. Avoid smoking, eating and drinking during use. Wash with soap and water after handling. Containers of this material may contain hazardous residues when emptied. Do not use on hot vehicles.</p>
      <p class="narrow"><span class="info__head">STORAGE &amp; DISPOSAL:</span> Keep in a cool place out of the sun. Do not store above 50˚C. Dispose of cans thoughtfully or via an authorised chemical waste facility. MSDS available upon request.</p>
    </div>

    <svg class="ghs ghs--exclaim" viewBox="0 0 100 100" role="img" aria-label="GHS exclamation mark pictogram">
      <polygon points="50,4 96,50 50,96 4,50" fill="#fff" stroke="var(--ghs-red)" stroke-width="7" stroke-linejoin="round"/>
      <rect x="44" y="24" width="12" height="36" rx="3" fill="#000"/>
      <circle cx="50" cy="71" r="6.5" fill="#000"/>
    </svg>
    <svg class="ghs ghs--flame" viewBox="0 0 100 100" role="img" aria-label="GHS flame pictogram">
      <polygon points="50,4 96,50 50,96 4,50" fill="#fff" stroke="var(--ghs-red)" stroke-width="7" stroke-linejoin="round"/>
      <path d="M50 22 C58 34 66 40 64 54 C63 62 57 67 50 67 C42 67 36 61 37 52 C38 45 43 42 44 35 C47 40 47 45 50 47 C53 40 50 30 50 22 Z" fill="#000"/>
      <rect x="32" y="70" width="36" height="5" fill="#000"/>
    </svg>
    <div class="ghs-note ghs-note--flame">KEEP AWAY FROM<br>NAKED FLAME</div>
    <div class="ghs-note ghs-note--un">AEROSOLS UN1950</div>

    <div class="back-mascot" role="img" aria-label="Brand mascot illustration"></div>
    <div class="back-brand">BRACKENMOOR</div>
    <address class="company">
      A product of Brackenmoor Australia Pty Ltd<br>
      ABN: 48 317 205 964<br>
      7/318 Kestrel Avenue FERNCLIFF VIC 3187<br>
      AUSTRALIA<br>
      Phone: +61 3 9184 5362<br>
      www.brackenmoorstore.com.au<br>
      <span class="company__code">Product Code: BRKM350TDE</span>
    </address>

    <div class="label__bleed"></div>
  </section>
</main>
</body>
</html>
```